Valbrook Data Works

Our company is about IT hardwares and IT solutions. IT hardware such as PC, RAMS, storage and servers. IT solutions such as project management, BA. We are also selling new technology too.

Target Market(s)

Consumer, Small to Medium Business, Corporate

Requirements
Must have
• The business card must have the following:
• Name:
• Title:
• Contact Number:
• Email address:
• Website:
• Color: Must match the logo color upgrade

```html
<!DOCTYPE html>
<html lang="en">
<head>
<meta charset="utf-8">
<title>Valbrook Data Works – Business Card</title>
<link href="https://fonts.googleapis.com/css2?family=Khand:wght@500;600&family=Roboto:wght@400&display=swap" rel="stylesheet">
<style>
  :root {
    --backdrop: #e2e2e2;
    --card-light: #f6f6f6;
    --card-dark: #444444;
    --ink: #444444;
    --ink-soft: #4a4a4a;
    --accent: #d4832c;
    --accent-light: #d68f3a;
    --accent-deep: #b9602a;
    --rule: #9a9a9a;
    --white: #ffffff;
  }
  html, body {
    margin: 0;
    padding: 0;
    width: 1200px;
    height: 960px;
    overflow: hidden;
    background: var(--backdrop);
  }
  .canvas {
    position: relative;
    width: 1200px;
    height: 960px;
  }
  .card {
    position: absolute;
    width: 601px;
    height: 343px;
    box-sizing: border-box;
    overflow: hidden;
  }
  .card--front {
    left: 314px;
    top: 113px;
    background: var(--card-light);
  }
  .card--back {
    left: 311px;
    top: 472px;
    background: var(--card-dark);
  }
  .brand {
    position: absolute;
    right: 44px;
    top: 40px;
    display: flex;
    flex-direction: column;
    align-items: flex-end;
    gap: 30px;
  }
  .brand__mark {
    width: 30px;
    height: 30px;
    background: var(--accent);
    margin-right: 95px;
  }
  .brand__name {
    font-family: "Khand", "Arial Narrow", sans-serif;
    font-weight: 600;
    font-size: 36px;
    line-height: 1;
    letter-spacing: 0.5px;
    color: var(--ink);
    text-transform: uppercase;
    margin: 0;
  }
  .person {
    position: absolute;
    left: 42px;
    top: 178px;
    width: 515px;
  }
  .person__name {
    font-family: "Khand", "Arial Narrow", sans-serif;
    font-weight: 600;
    font-size: 35px;
    line-height: 1;
    color: var(--ink);
    text-transform: uppercase;
    margin: 0;
  }
  .person__title {
    font-family: "Khand", "Arial Narrow", sans-serif;
    font-weight: 600;
    font-size: 19px;
    line-height: 1;
    color: var(--accent);
    text-transform: uppercase;
    margin: 0;
  }
  .person__rule {
    border: 0;
    border-top: 1px solid var(--rule);
    margin: 9px 0 11px;
  }
  .contact {
    list-style: none;
    margin: 0;
    padding: 0;
  }
  .contact__item {
    display: flex;
    align-items: center;
    gap: 7px;
    font-family: "Roboto", sans-serif;
    font-size: 14.5px;
    line-height: 19.5px;
    color: var(--ink-soft);
  }
  .contact__icon {
    width: 13px;
    height: 13px;
    fill: var(--ink-soft);
    flex: none;
  }
  .card__pattern {
    position: absolute;
    left: 0;
    top: 0;
    width: 372px;
    height: 343px;
    background: linear-gradient(120deg, var(--accent-light), var(--accent-deep));
  }
  .card__web {
    position: absolute;
    right: 44px;
    top: 124px;
    font-family: "Khand", "Arial Narrow", sans-serif;
    font-weight: 600;
    font-size: 21px;
    line-height: 1;
    color: var(--white);
    margin: 0;
  }
</style>
</head>
<body>
<main class="canvas">
  <section class="card card--front" aria-label="Business card front">
    <div class="brand">
      <span class="brand__mark" aria-hidden="true"></span>
      <p class="brand__name">Valbrook Data Works</p>
    </div>
    <div class="person">
      <h1 class="person__name">Daniel Reyes</h1>
      <p class="person__title">CEO/Founder</p>
      <hr class="person__rule">
      <ul class="contact">
        <li class="contact__item">
          <svg class="contact__icon" viewBox="0 0 16 16" aria-hidden="true"><path d="M3.6 1.2l2.3 2.6-1.3 1.9c.9 2 2.5 3.6 4.6 4.6l1.9-1.3 2.6 2.3-1.2 2.3C7 13.3 2.7 9 1.2 3.4z"/></svg>
          555 210 4837
        </li>
        <li class="contact__item">
          <svg class="contact__icon" viewBox="0 0 16 16" aria-hidden="true"><path d="M1 3.5h14v1.2L8 9 1 4.7z"/><path d="M1 6.2l7 4.3 7-4.3V12.5H1z"/></svg>
          daniel@valbrookdata.com
        </li>
        <li class="contact__item">
          <svg class="contact__icon" viewBox="0 0 16 16" aria-hidden="true"><circle cx="8" cy="8" r="7"/><path d="M5 4.5c1.5.3 2.2 1.3 1.7 2.4-.5 1 .3 1.8 1.3 2.2.8.4.6 1.7-.2 2.8C5.3 11.5 4 9.7 3.6 7.8 3.4 6.5 4 5.2 5 4.5zM10.5 3.8c1.4.8 2.2 2.4 2 4-.9-.2-1.7-.8-1.8-1.8-.1-.9-.5-1.6-.2-2.2z" fill="#f6f6f6"/></svg>
          www.valbrookdata.com
        </li>
      </ul>
    </div>
  </section>

  <section class="card card--back" aria-label="Business card back">
    <div class="card__pattern" role="img" aria-label="Large orange brand graphic area"></div>
    <p class="card__web">www.valbrookdata.com</p>
  </section>
</main>
</body>
</html>
```